Business Card Design Project

New Business Card design for Travorel Technology Ltd using new Logo and new Tagline for staffing company.

About us from our website - www.travorel-example.net:

TraVorel is a leading and recognized Electronic Entertainment, Workforce Augmentation, and Project Management solutions provider with clients in Electronic Entertainment, Legal, Technology, Government and other verticals that range in size from start up organizations to Zentora 300 companies. TraVorel is certified as an 8(a) minority and woman owned enterprise, established in 1998.

Target Market(s)

Companies in Electronic Entertainment, Legal, Government and Technology

Industry/Entity Type

Business

Requirements
Must have
• Must include in small letters the following information on back:

Established in 1998
8(a)(w)(e), Cage #7KQW4, DUNS #412306957

Front should have the following:
Dale Merrow
Vice President
5870 Brookhollow Court
Lindenvale, QX 908172
555-318-2046 X 100
555-742-9813 Fax
555-318-2046 Toll Free
name@travorel-example.net

Our Tagline: Connect • Collaborate • Achieve

```html
<!DOCTYPE html>
<html lang="en">
<head>
<meta charset="utf-8">
<title>TraVorel Technology Ltd — Business Card Back</title>
<link rel="stylesheet" href="https://fonts.googleapis.com/css2?family=Josefin+Sans:wght@300;400&family=Montserrat:wght@700&display=swap">
<style>
  :root {
    --page-bg: #ffffff;
    --label-ink: #1a1a1a;
    --card-bg: #141414;
    --texture-tone: #191919;
    --logo-ink: #ffffff;
    --accent-blue: #1f5fae;
    --fine-print: #cfcfcf;
  }
  * { margin: 0; padding: 0; box-sizing: border-box; }
  html, body {
    width: 1200px;
    height: 737px;
    overflow: hidden;
    background: var(--page-bg);
  }
  .sheet {
    position: relative;
    width: 1200px;
    height: 737px;
  }
  .side-label {
    position: absolute;
    top: 4px;
    left: 0;
    width: 100%;
    text-align: center;
    font-family: "Josefin Sans", sans-serif;
    font-weight: 300;
    font-size: 46px;
    letter-spacing: 3px;
    color: var(--label-ink);
  }
  .card {
    position: absolute;
    left: 12px;
    top: 96px;
    width: 1172px;
    height: 636px;
    background: var(--card-bg);
    overflow: hidden;
  }
  .card-texture {
    position: absolute;
    inset: 0;
    background: linear-gradient(180deg, var(--texture-tone), var(--card-bg) 50%, var(--texture-tone));
  }
  .brand {
    position: absolute;
    top: 262px;
    left: 0;
    width: 100%;
    display: flex;
    align-items: center;
    justify-content: center;
    gap: 22px;
  }
  .brand-dot {
    width: 34px;
    height: 34px;
    border-radius: 50%;
    background: var(--accent-blue);
  }
  .brand-name {
    font-family: "Montserrat", sans-serif;
    font-weight: 700;
    font-size: 112px;
    line-height: 1;
    letter-spacing: -2px;
    color: var(--logo-ink);
  }
  .credentials {
    position: absolute;
    top: 492px;
    left: 0;
    width: 100%;
    text-align: center;
    font-family: "Josefin Sans", sans-serif;
    font-weight: 400;
    font-size: 17px;
    line-height: 28px;
    letter-spacing: 2px;
    font-variant: small-caps;
    color: var(--fine-print);
  }
</style>
</head>
<body>
  <main class="sheet">
    <h1 class="side-label">BACK</h1>
    <section class="card">
      <div class="card-texture" role="img" aria-label="Faint repeating text texture across the card background"></div>
      <div class="brand">
        <span class="brand-dot" aria-hidden="true"></span>
        <span class="brand-name">TraVorel</span>
      </div>
      <div class="credentials">
        <p>Established in 1998</p>
        <p>8(a)(w)(e), Cage #7KQW4, DUNS #412306957</p>
      </div>
    </section>
  </main>
</body>
</html>
```